Post card design for pool service company

This card is for getting pool owners to call us concerning pool service. Post card size is 6"x8" printed. My website is tidewhisk.net for additional information and color schemes. I want the card to compliment our logo colors. I've uploaded a design I like, but I want it to be unique rather than simply copied. Can you improve on the design sample I've included? I included logo and our wrapped truck which I would like incorporated into the post card. The truck pic can be whole or partial, as long as the name and pic is visible. Thanks!

Target Market(s)

Swimming pool owners looking for pool service

Industry/Entity Type

Swimming pool service

Colors
0054AA
0677BA
7BADD7
CADEEF
E8F1F8
EE7325
F08F49
F5BC92
FAE3D3
FDF4ED

Requirements
Must have
• Truck (partial ok, or full picture). Phone number is 619-382-7096. I'd like the card to let the client know they can either call or text. Also include the logo front and back where appropriate.
Nice to have
• A different picture than the one in the example that is uploaded.

```html
<!DOCTYPE html>
<html lang="en">
<head>
<meta charset="utf-8">
<title>Tidewhisk Pool Service Postcard</title>
<link rel="stylesheet" href="https://fonts.googleapis.com/css2?family=Fira+Sans:wght@400;500;600;700;800&display=swap">
<style>
  :root {
    --navy: #1c4a86;
    --mid-blue: #1d79bd;
    --sky: #5cc6e8;
    --flame: #e5401f;
    --white: #ffffff;
    --line: #d5d9de;
    --backdrop: #7d7d7d;
  }
  * { margin: 0; padding: 0; box-sizing: border-box; }
  html, body {
    width: 1200px; height: 904px; overflow: hidden;
    background: var(--backdrop);
    font-family: "Fira Sans", sans-serif;
  }
  .postcard {
    position: absolute;
    width: 518px; height: 388px;
    overflow: hidden;
    background: var(--white);
    box-shadow: 0 3px 10px rgba(0,0,0,.25);
  }
  .postcard--front { left: 205px; top: 47px; }
  .postcard--back  { left: 478px; top: 469px; }
  .postcard__art { position: absolute; inset: 0; width: 518px; height: 388px; }
  .txt { position: absolute; left: 29px; color: var(--white); white-space: nowrap; }
  .accent { color: var(--sky); }

  .headline { top: 24px; font-size: 34px; line-height: 38px; font-weight: 800; letter-spacing: -0.2px; }
  .subline { top: 166px; font-size: 15px; line-height: 20px; font-weight: 700; }
  .cta { top: 261px; font-size: 20px; line-height: 25.5px; font-weight: 800; }

  .contact { display: flex; align-items: center; font-weight: 600; }
  .contact svg { flex: none; }
  .contact__item { display: flex; align-items: center; gap: 4px; }
  .postcard--front .contact { top: 349px; font-size: 15px; gap: 14px; }
  .postcard--back .contact { top: 358px; font-size: 14px; gap: 12px; }

  .brand {
    position: absolute; display: flex; align-items: center; gap: 6px;
    color: var(--navy); font-weight: 800; white-space: nowrap;
  }
  .brand__dot { border-radius: 50%; background: var(--flame); flex: none; }
  .postcard--front .brand { left: 385px; top: 305px; font-size: 22px; }
  .postcard--front .brand__dot { width: 16px; height: 16px; }
  .postcard--back .brand { left: 300px; top: 42px; font-size: 16px; }
  .postcard--back .brand__dot { width: 12px; height: 12px; }

  .plan { top: 23px; font-size: 18px; line-height: 24px; font-weight: 800; color: var(--sky); }
  .price { top: 71px; font-size: 25px; line-height: 28px; font-weight: 800; }
  .price-note { top: 101px; left: 31px; font-size: 12px; line-height: 14px; font-weight: 400; }
  .includes-title { top: 141px; font-size: 11px; line-height: 14.5px; font-weight: 700; }
  .includes { top: 173px; list-style: none; font-size: 9.5px; line-height: 16.3px; font-weight: 500; }
  .includes li { display: flex; align-items: center; gap: 5px; }

  .stamp { position: absolute; left: 434px; top: 22px; width: 61px; height: 56px; border: 1px solid var(--line); }
  .address-line { position: absolute; right: 23px; height: 1px; background: var(--line); }
</style>
</head>
<body>

<!-- Front -->
<section class="postcard postcard--front">
  <svg class="postcard__art" viewBox="0 0 518 388" aria-hidden="false">
    <defs>
      <radialGradient id="poolWater" cx="55%" cy="45%" r="60%">
        <stop offset="0%" stop-color="#f0b7a0"/>
        <stop offset="35%" stop-color="#4fc3e6"/>
        <stop offset="100%" stop-color="#1a86c2"/>
      </radialGradient>
    </defs>
    <rect width="518" height="388" fill="var(--white)"/>
    <ellipse role="img" aria-label="Photo of two smiling children in swim goggles splashing in a bright blue pool" cx="400" cy="115" rx="215" ry="190" fill="url(#poolWater)"/>
    <path d="M0 0 H237 C283 55 300 145 285 205 C272 255 240 285 195 300 L0 300 Z" fill="var(--navy)"/>
    <path d="M0 243 C70 220 175 218 245 244 C305 266 348 318 380 388 L368 388 C335 320 295 270 240 250 C170 226 70 228 0 251 Z" fill="var(--sky)"/>
    <path d="M0 251 C70 228 170 226 240 250 C295 270 335 320 368 388 L0 388 Z" fill="var(--flame)"/>
    <path d="M29 155 q4.5 -3 9 0 t9 0 t9 0 t9 0 t9 0 t9 0 t9 0 t9 0 t9 0 t9 0 t9 0 t9 0 t9 0 t9 0 t9 0 t9 0 t9 0 t9 0 t9 0 t9 0 t9 0 t9 0 t9 0 t9 0" fill="none" stroke="var(--sky)" stroke-width="1.2"/>
  </svg>

  <h1 class="txt headline">KEEP YOUR<br><span class="accent">POOL BLUE</span> ALL<br>YEAR ROUND!</h1>
  <p class="txt subline">Weekly &amp; Bi-weekly swimming<br>pool maintenance &amp; services</p>
  <p class="txt cta">CALL OR TEXT US<br><span class="accent">TODAY TO SCHEDULE</span><br>YOUR FREE <span class="accent">POOL QUOTE!</span></p>

  <div class="txt contact">
    <span class="contact__item">
      <svg width="13" height="13" viewBox="0 0 24 24"><path d="M6.6 10.8a15.2 15.2 0 0 0 6.6 6.6l2.2-2.2a1 1 0 0 1 1-.25 11.4 11.4 0 0 0 3.6.57 1 1 0 0 1 1 1V20a1 1 0 0 1-1 1A17 17 0 0 1 3 4a1 1 0 0 1 1-1h3.5a1 1 0 0 1 1 1c0 1.25.2 2.45.57 3.57a1 1 0 0 1-.25 1z" fill="var(--sky)"/></svg>
      (619) 382-7096
    </span>
    <span class="contact__item">
      <svg width="13" height="13" viewBox="0 0 24 24" fill="none" stroke="var(--sky)" stroke-width="2"><circle cx="12" cy="12" r="9"/><path d="M3 12h18M12 3c3 3 3 15 0 18M12 3c-3 3-3 15 0 18"/></svg>
      www.tidewhisk.net
    </span>
  </div>

  <div class="brand"><span class="brand__dot"></span>Tidewhisk</div>
</section>

<!-- Back -->
<section class="postcard postcard--back">
  <svg class="postcard__art" viewBox="0 0 518 388">
    <defs>
      <linearGradient id="mascotTone" x1="0" y1="0" x2="0" y2="1">
        <stop offset="0%" stop-color="#3a7fc4"/>
        <stop offset="100%" stop-color="#e9782f"/>
      </linearGradient>
      <linearGradient id="truckTone" x1="0" y1="0" x2="1" y2="0">
        <stop offset="0%" stop-color="#e8822f"/>
        <stop offset="55%" stop-color="#2f7fd0"/>
        <stop offset="100%" stop-color="#e8822f"/>
      </linearGradient>
    </defs>
    <rect width="518" height="388" fill="var(--white)"/>
    <rect width="150" height="388" fill="var(--navy)"/>
    <circle cx="145" cy="150" r="170" fill="var(--navy)"/>
    <path d="M0 0 H240 C230 70 190 125 110 135 C70 140 30 137 0 133 Z" fill="var(--mid-blue)"/>
    <rect role="img" aria-label="Illustration of the pool technician mascot holding a skimmer net and giving a thumbs up" x="206" y="58" width="116" height="218" rx="40" fill="url(#mascotTone)"/>
    <path d="M0 297 C90 280 195 296 275 322 C318 338 350 362 372 388 L358 388 C336 364 304 344 262 330 C185 303 80 290 0 305 Z" fill="var(--sky)"/>
    <path d="M0 305 C80 290 185 303 262 330 C304 344 336 364 358 388 L0 388 Z" fill="var(--flame)"/>
    <rect role="img" aria-label="Photo of the company's wrapped pickup truck with branding and phone number" x="27" y="257" width="282" height="95" rx="14" fill="url(#truckTone)"/>
    <rect x="336" y="166" width="159" height="1" fill="var(--line)"/>
    <rect x="330" y="205" width="165" height="1" fill="var(--line)"/>
    <rect x="318" y="243" width="177" height="1" fill="var(--line)"/>
  </svg>

  <h2 class="txt plan">OUR MOST POPULAR<br>PLAN STARTS AT</h2>
  <p class="txt price">ONLY $125</p>
  <p class="txt price-note">(MOST POOLS)</p>

  <p class="txt includes-title">Our pool maintenance<br>always includes:</p>
  <ul class="txt includes">
    <li><svg width="9" height="9" viewBox="0 0 12 12" fill="none" stroke="var(--sky)" stroke-width="1.4"><rect x="1" y="1" width="10" height="10" rx="1.5"/><path d="M3.3 6.2l2 2 3.6-4.2"/></svg>Full service including chemicals</li>
    <li><svg width="9" height="9" viewBox="0 0 12 12" fill="none" stroke="var(--sky)" stroke-width="1.4"><rect x="1" y="1" width="10" height="10" rx="1.5"/><path d="M3.3 6.2l2 2 3.6-4.2"/></svg>Same day, same pool technician</li>
    <li><svg width="9" height="9" viewBox="0 0 12 12" fill="none" stroke="var(--sky)" stroke-width="1.4"><rect x="1" y="1" width="10" height="10" rx="1.5"/><path d="M3.3 6.2l2 2 3.6-4.2"/></svg>“No Green Pool” guarantee</li>
    <li><svg width="9" height="9" viewBox="0 0 12 12" fill="none" stroke="var(--sky)" stroke-width="1.4"><rect x="1" y="1" width="10" height="10" rx="1.5"/><path d="M3.3 6.2l2 2 3.6-4.2"/></svg>5-star customer service</li>
    <li><svg width="9" height="9" viewBox="0 0 12 12" fill="none" stroke="var(--sky)" stroke-width="1.4"><rect x="1" y="1" width="10" height="10" rx="1.5"/><path d="M3.3 6.2l2 2 3.6-4.2"/></svg>Pet friendly (Woof!)</li>
  </ul>

  <div class="txt contact">
    <span class="contact__item">
      <svg width="12" height="12" viewBox="0 0 24 24"><path d="M6.6 10.8a15.2 15.2 0 0 0 6.6 6.6l2.2-2.2a1 1 0 0 1 1-.25 11.4 11.4 0 0 0 3.6.57 1 1 0 0 1 1 1V20a1 1 0 0 1-1 1A17 17 0 0 1 3 4a1 1 0 0 1 1-1h3.5a1 1 0 0 1 1 1c0 1.25.2 2.45.57 3.57a1 1 0 0 1-.25 1z" fill="var(--sky)"/></svg>
      (619) 382-7096
    </span>
    <span class="contact__item">
      <svg width="12" height="12" viewBox="0 0 24 24" fill="none" stroke="var(--sky)" stroke-width="2"><circle cx="12" cy="12" r="9"/><path d="M3 12h18M12 3c3 3 3 15 0 18M12 3c-3 3-3 15 0 18"/></svg>
      www.tidewhisk.net
    </span>
  </div>

  <div class="brand"><span class="brand__dot"></span>Tidewhisk</div>
  <div class="stamp"></div>
</section>

</body>
</html>
```